Business card for utility of the future

I need a business card template designed for brookvane. We provide sustainable water, energy and waste services to homes.

The card should include name, position, email address, phone number, website and our logo (attached). I would like it to convey professionalism and creativity.

Target Market(s)

Homeowners, investors, corporate partners.

Industry/Entity Type

Utility

Contact Information for Business Card

The card should include name, position, email address, phone number, website and our logo (attached).

```html
<!DOCTYPE html>
<html lang="en">
<head>
<meta charset="utf-8">
<title>brookvane business card</title>
<link rel="stylesheet" href="https://fonts.googleapis.com/css2?family=Source+Sans+3:wght@400;600;700&display=swap">
<style>
  :root {
    --backdrop: #8e8e8e;
    --paper: #f3f3f1;
    --brand-green: #5aa66f;
    --brand-green-soft: #63ad77;
    --accent-orange: #de6f4d;
    --ink: #3d3d3d;
    --rule: #6f6f6f;
    --on-green: #f2f6f3;
  }
  * { margin: 0; padding: 0; box-sizing: border-box; }
  html, body {
    width: 1105px;
    height: 1200px;
    overflow: hidden;
    background: var(--backdrop);
    font-family: "Source Sans 3", sans-serif;
  }
  .card {
    position: absolute;
    left: 180px;
    width: 746px;
    height: 427px;
    overflow: hidden;
  }
  .card-front { top: 119px; background: var(--paper); }
  .card-back  { top: 636px; background: var(--brand-green); }

  .wordmark {
    position: absolute;
    right: 31px;
    top: 52px;
    color: var(--brand-green);
    font-weight: 700;
    font-size: 76px;
    line-height: 1;
    letter-spacing: -1px;
  }

  .holder-name {
    position: absolute;
    left: 40px;
    top: 236px;
    color: var(--brand-green);
    font-weight: 600;
    font-size: 28px;
    line-height: 1;
  }
  .holder-role {
    position: absolute;
    left: 40px;
    top: 272px;
    color: var(--accent-orange);
    font-size: 21px;
    line-height: 1;
  }
  .divider {
    position: absolute;
    left: 40px;
    top: 299px;
    width: 675px;
    height: 2px;
    background: var(--rule);
  }
  .contact-list {
    position: absolute;
    left: 40px;
    top: 315px;
    list-style: none;
    color: var(--ink);
    font-size: 20px;
    line-height: 29px;
  }
  .contact-item { display: flex; align-items: center; gap: 14px; }
  .contact-icon { width: 18px; height: 18px; fill: var(--brand-green); }

  .footer-bands { position: absolute; left: 0; top: 0; width: 746px; height: 427px; }
  .footer-url {
    position: absolute;
    right: 28px;
    top: 392px;
    color: var(--on-green);
    font-size: 20px;
    letter-spacing: 2px;
    line-height: 1;
  }

  .back-texture {
    position: absolute;
    inset: 0;
    background: linear-gradient(180deg, var(--brand-green-soft), var(--brand-green));
  }
  .back-url {
    position: absolute;
    left: 0;
    right: 0;
    top: 196px;
    text-align: center;
    color: var(--on-green);
    font-size: 27px;
    letter-spacing: 7px;
    line-height: 1;
  }
</style>
</head>
<body>

<section class="card card-front">
  <p class="wordmark">brookvane</p>

  <p class="holder-name">Evan Hale</p>
  <p class="holder-role">CEO/Founder</p>
  <div class="divider"></div>

  <ul class="contact-list">
    <li class="contact-item">
      <svg class="contact-icon" viewBox="0 0 24 24" aria-hidden="true"><path d="M6.6 10.8c1.4 2.8 3.8 5.1 6.6 6.6l2.2-2.2c.3-.3.7-.4 1-.2 1.1.4 2.3.6 3.6.6.6 0 1 .4 1 1V20c0 .6-.4 1-1 1C10.6 21 3 13.4 3 4c0-.6.4-1 1-1h3.5c.6 0 1 .4 1 1 0 1.3.2 2.5.6 3.6.1.3 0 .7-.2 1l-2.3 2.2z"/></svg>
      <span>555 214 7830</span>
    </li>
    <li class="contact-item">
      <svg class="contact-icon" viewBox="0 0 24 24" aria-hidden="true"><path d="M2 5h20v14H2z M3.5 6.5 12 12.5l8.5-6z" fill-rule="evenodd"/></svg>
      <span>name@brookvane.com</span>
    </li>
  </ul>

  <svg class="footer-bands" viewBox="0 0 746 427" aria-hidden="true">
    <path d="M0 400 H456 L446 410 H0 Z" fill="var(--accent-orange)"/>
    <path d="M0 410 H446 C462 410 460 383 490 383 H746 V427 H0 Z" fill="var(--brand-green)"/>
  </svg>
  <p class="footer-url">www.brookvane.com</p>
</section>

<section class="card card-back">
  <div class="back-texture" role="img" aria-label="Faint repeating brand name texture in green tones"></div>
  <p class="back-url">WWW.BROOKVANE.COM</p>
</section>

</body>
</html>
```